Business Card/ Car Magnet/ Polo Shirt/ Envelope/ Letterhead Design Project
Birchmont Property Valuations, LLC.
Business Card/ Car Magnet/ Polo Shirt/ Envelope/ Letterhead Design Project - Real Estate
Creative Brief
Professional
Gus Talbottine
State Certified Residential Real Estate Appraiser
14 Coldmeadow Ln Sewell, NJ 08080
gtalbottine@birchmontvaluations.example
valuemarkhq.example
NJ- 57RC00913400 PA- RL284615 DE- X2-0000317
Please be creative...
gust1983 gust1983
Hello, Just wanted to clarify some of the common questions asked so far. The colors to incorporate would be blue, green and white (unless of course you would like to incorporate other colors for creativity) . please feel free to incorporate them any way you see fit. The polo shirts will be done on white, black and royal blue shirts. Please be as creative as you like. Thanks you for your efforts and for participating! Please reply back with any further questions. Thanks! BPV

```html
<!DOCTYPE html>
<html lang="en">
<head>
<meta charset="utf-8">
<title>Birchmont Property Valuations – Business Card</title>
<link rel="stylesheet" href="https://fonts.googleapis.com/css2?family=Open+Sans:wght@400;600;700&display=swap">
<style>
  :root {
    --bg: #c9cacc;
    --card: #ffffff;
    --navy: #1f3f7a;
    --blue: #2a6db5;
    --blue-light: #3c8fd6;
    --green: #5fae3a;
    --green-light: #a6d14a;
    --text: #3a3f47;
  }
  * { box-sizing: border-box; margin: 0; padding: 0; }
  html, body { width: 1200px; height: 878px; overflow: hidden; }
  body {
    background: var(--bg);
    font-family: "Open Sans", Arial, sans-serif;
    position: relative;
  }
  .card {
    position: absolute;
    width: 520px;
    height: 298px;
    background: var(--card);
    box-shadow: 0 2px 6px rgba(0,0,0,0.18);
    overflow: hidden;
  }
  .card--back { left: 50px; top: 290px; }
  .card--front { left: 630px; top: 290px; }

  .card__bands { position: absolute; inset: 0; }

  .brand { position: absolute; color: var(--navy); }
  .brand__row { display: flex; align-items: center; gap: 8px; }
  .brand__dot {
    width: 18px; height: 18px; border-radius: 50%;
    background: var(--green);
  }
  .brand__name { font-weight: 600; font-size: 40px; letter-spacing: 3px; line-height: 1; }
  .brand__full { font-weight: 600; font-size: 9.5px; letter-spacing: 0.6px; text-transform: uppercase; margin-top: 5px; }

  .card--back .brand { left: 34px; top: 62px; }

  .card--front .brand { right: 34px; bottom: 48px; text-align: right; }
  .card--front .brand__row { justify-content: flex-end; }

  .contact { position: absolute; left: 272px; top: 92px; color: var(--text); }
  .contact__name { font-weight: 700; font-size: 15px; color: #222; }
  .contact__title { font-size: 10.5px; color: var(--text); margin-bottom: 10px; }
  .contact__address { font-size: 10px; line-height: 1.35; margin-bottom: 10px; }
  .contact__list { list-style: none; font-size: 10px; line-height: 1.5; }
  .contact__list li { display: flex; align-items: center; gap: 6px; }
  .contact__list svg { width: 9px; height: 9px; fill: var(--navy); flex: none; }

  .website {
    position: absolute; right: 22px; bottom: 7px;
    color: #fff; font-size: 11px; letter-spacing: 0.3px;
  }
</style>
</head>
<body>

  <section class="card card--back" aria-label="Business card, contact side">
    <svg class="card__bands" viewBox="0 0 520 298" aria-hidden="true">
      <defs>
        <linearGradient id="edgeGreen" x1="0" y1="0" x2="0" y2="1">
          <stop offset="0" stop-color="#a6d14a"/>
          <stop offset="1" stop-color="#3f9a3a"/>
        </linearGradient>
        <linearGradient id="bandBlue" x1="0" y1="0" x2="1" y2="0">
          <stop offset="0" stop-color="#3c8fd6"/>
          <stop offset="1" stop-color="#1f5aa8"/>
        </linearGradient>
        <linearGradient id="bandGreen" x1="0" y1="0" x2="1" y2="0">
          <stop offset="0" stop-color="#3f9a3a"/>
          <stop offset="1" stop-color="#a6d14a"/>
        </linearGradient>
      </defs>
      <rect x="0" y="150" width="7" height="148" fill="url(#edgeGreen)"/>
      <polygon points="0,262 150,262 130,298 0,298" fill="url(#bandGreen)"/>
      <polygon points="150,268 520,268 520,298 134,298" fill="url(#bandBlue)"/>
    </svg>

    <div class="brand">
      <div class="brand__row">
        <span class="brand__name">BPV</span>
        <span class="brand__dot"></span>
      </div>
      <div class="brand__full">Birchmont Property Valuations, LLC.</div>
    </div>

    <div class="contact">
      <p class="contact__name">Gus Talbottine</p>
      <p class="contact__title">Managing Director</p>
      <p class="contact__address">14 Coldmeadow Ln<br>Sewell, NJ 08080</p>
      <ul class="contact__list">
        <li><svg viewBox="0 0 10 10"><path d="M2 0.5 L3.6 0.5 L4.3 2.8 L3.2 3.6 Q4 5.8 6.4 6.8 L7.2 5.7 L9.5 6.4 L9.5 8 Q9.5 9.5 8 9.5 Q0.5 9 0.5 2 Q0.5 0.5 2 0.5 Z"/></svg>123 456 7890</li>
        <li><svg viewBox="0 0 10 10"><rect x="2.5" y="0" width="5" height="10" rx="1"/><rect x="3.3" y="1.2" width="3.4" height="6.2" fill="#fff"/></svg>123 456 7890</li>
        <li><svg viewBox="0 0 10 10"><rect x="2.5" y="0.5" width="5" height="3"/><rect x="0.5" y="3.5" width="9" height="4.5" rx="0.8"/><rect x="2.5" y="6.5" width="5" height="3"/></svg>123 456 7890</li>
        <li><svg viewBox="0 0 10 10"><rect x="0.5" y="2" width="9" height="6.5"/><path d="M0.8 2.3 L5 5.6 L9.2 2.3" fill="none" stroke="#fff" stroke-width="0.9"/></svg>gtalbottine@birchmontvaluations.example</li>
      </ul>
    </div>

    <p class="website">www.valuemarkhq.example</p>
  </section>

  <section class="card card--front" aria-label="Business card, brand side">
    <div class="brand">
      <div class="brand__row">
        <span class="brand__dot"></span>
        <span class="brand__name">BPV</span>
      </div>
      <div class="brand__full">Birchmont Property Valuations, LLC.</div>
    </div>
  </section>

</body>
</html>
```